Corporate Design für jur. Repetitorium
Extrem professionell, freundlich und hilfsbereit. Die Designs hatten stets eine sehr hohe Qualität und wurden, egal um welche Idee oder Variation es sich auch gehandelt hat, mehrfach ohne Beanstandung und nahezu umgehend modifiziert. Ich kann die Zusammenarbeit nur loben und hervorheben und gebe an dieser Stelle den sechsten Stern! Weiter so!
Zielgruppe
Wir sind ein jur. Repetitorium und bieten Individual- und Gruppenunterricht für Studenten an, die sich auf ihre Prüfungen vorbereiten. Unsere Zielgruppe liegt daher bei Studiumsanfängern und Fortgeschrittenen. Alter ca. 19 - 27. Primär visieren wir Studenten an, die bereit sind für kleinen Gruppen- sowie Individualunterricht etwas mehr zu zahlen. Wir sind ein international ausgerichtetes Unternehmen. Neben Studenten- bieten wir des weiteren auch jur. Weiterbildungskurse für fertige Anwälte an. Wichtig ist uns ein moderner und aufgeschlossener Auftritt, der sich von dem sehr langweiligen und konservativen Image gängiger Kanzleien und Repetitorien abhebt. Jung, modern und frisch wollen wir wirken da wir ein junges Team sind.
Aufgabenstellung
Wir wollen seriös aber nicht zu ernst wirken, professionell, persönlich, eine entspannte und effektive Lernatmosphäre bietend. Es soll ein gutes persönliches Gefühl entstehen, ein sorgenfreier aber leistungsorientierter Lernflair der sich von der normalen Lernumgebung abhebt. Auch unser Corporate Design soll diese Einstellung zeigen. Da wir mit modernen Medien wie Korvs , Quimbo Stylos, Beamer, Cloud und online Tutoring arbeiten, sollte dies auch im Design Ausdruck finden. Wir sind im Vergleich zu anderen Anbietern international aufgestellt, da wir sowohl das nationale deutsche Recht anbieten, aber auch europäisches Recht, sowie Rechtvergleichung mit andern Rechtssystemen. Dieses Konzept und die damit verbundene Internationalität, kann gerne im Design eingebracht werden. Sehr gut gefällt uns z.B. der Auftritt von Quimbo.
Gerne mit silber-, weißtönen, grau, platin:)

```html
<!DOCTYPE html>
<html lang="de">
<head>
<meta charset="utf-8">
<title>Visitenkarten – abstrakter Paragraph</title>
<link rel="stylesheet" href="https://fonts.googleapis.com/css2?family=Jura:wght@400;500&family=Montserrat:wght@300&family=PT+Sans&display=swap">
<style>
  :root {
    --page: #ffffff;
    --ink: #333333;
    --card: #363636;
    --light: #e8e8e8;
    --green: #95bf2b;
  }
  * { margin: 0; padding: 0; box-sizing: border-box; }
  html, body { width: 1146px; height: 1200px; overflow: hidden; background: var(--page); }
  .sheet { position: relative; width: 1146px; height: 1200px; }

  .sheet-title {
    position: absolute; left: 0; top: 0;
    font: 500 46px/1 "Jura", sans-serif;
    letter-spacing: 3px; color: var(--ink);
  }
  .sheet-note {
    position: absolute; left: 751px; top: 153px; width: 395px;
    font: 500 37px/47px "Jura", sans-serif;
    letter-spacing: 2px; color: var(--ink);
  }

  .card {
    position: absolute; width: 311px; height: 479px;
    background: var(--card); overflow: hidden; color: var(--light);
  }
  .row-1 { top: 164px; }
  .row-2 { top: 720px; }
  .front { left: 38px; }
  .back { left: 380px; }

  .mark-circle { position: absolute; left: 65px; top: 62px; }

  .front .brand {
    position: absolute; left: 0; width: 100%; top: 282px; text-align: center;
    font-size: 31px; line-height: 1; letter-spacing: 0.5px; color: var(--light);
  }
  .front .tagline {
    position: absolute; left: 0; width: 100%; top: 323px; text-align: center;
    font: 300 10.5px/1 "Montserrat", sans-serif; color: #cfcfcf;
  }
  .front .address {
    position: absolute; left: 0; width: 100%; top: 376px; text-align: center;
    font-size: 13px; line-height: 17px;
  }
  .front .country {
    display: block; font-size: 9px; line-height: 9px; color: var(--green);
  }
  .front .web {
    position: absolute; left: 0; width: 100%; top: 434px; text-align: center;
    font-size: 18px; line-height: 1; color: var(--green);
  }

  .back .person {
    position: absolute; right: 23px; top: 125px; text-align: right;
  }
  .back .person-name { display: block; font-size: 19px; line-height: 20px; }
  .back .person-role { display: block; font-size: 9px; line-height: 11px; color: var(--green); }

  .back .contact {
    position: absolute; right: 23px; top: 365px; text-align: right;
  }
  .contact-item { margin-bottom: 6px; }
  .contact-label { display: block; font-size: 9px; line-height: 9px; color: var(--green); }
  .contact-value { display: block; font-size: 13px; line-height: 15px; }

  .type-sans { font-family: "PT Sans", sans-serif; }
  .type-tech { font-family: "Jura", sans-serif; }
  .type-sans .brand { font-family: "PT Sans", sans-serif; font-weight: 400; }
  .type-tech .brand { font-family: "PT Sans", sans-serif; font-weight: 400; }
  .type-tech .web { font-weight: 500; letter-spacing: 1px; }
</style>
</head>
<body>
<main class="sheet">
  <h1 class="sheet-title">Visitenkarten – abstrakter Paragraph</h1>

  <!-- Variante 1 -->
  <section class="card front row-1 type-sans">
    <svg class="mark-circle" width="180" height="180" viewBox="0 0 180 180" aria-hidden="true">
      <circle cx="90" cy="90" r="86" fill="none" stroke="var(--green)" stroke-width="2.5"/>
    </svg>
    <p class="brand">LEXARO</p>
    <p class="tagline">individual- &amp; gruppenrepetitorium</p>
    <p class="address">MUSTERSTRASSE 1<br>12345 BERLIN<span class="country">germany</span></p>
    <p class="web">www.lexaro.de</p>
  </section>

  <section class="card back row-1 type-sans">
    <p class="person"><span class="person-name">MAX MUSTERMANN</span><span class="person-role">seminarleiter</span></p>
    <div class="contact">
      <p class="contact-item"><span class="contact-label">telefon</span><span class="contact-value">+49 30 123 45 67</span></p>
      <p class="contact-item"><span class="contact-label">mobil</span><span class="contact-value">+49 171 123 45 67 89</span></p>
      <p class="contact-item"><span class="contact-label">mail</span><span class="contact-value">mustermann@lexaro.de</span></p>
    </div>
  </section>

  <!-- Variante 2 -->
  <section class="card front row-2 type-tech">
    <svg class="mark-circle" width="180" height="180" viewBox="0 0 180 180" aria-hidden="true">
      <circle cx="90" cy="90" r="86" fill="none" stroke="var(--green)" stroke-width="2.5"/>
    </svg>
    <p class="brand">LEXARO</p>
    <p class="tagline">individual- &amp; gruppenrepetitorium</p>
    <p class="address">MUSTERSTRASSE 1<br>12345 BERLIN<span class="country">germany</span></p>
    <p class="web">www.lexaro.de</p>
  </section>

  <section class="card back row-2 type-tech">
    <p class="person"><span class="person-name">MAX MUSTERMANN</span><span class="person-role">seminarleiter</span></p>
    <div class="contact">
      <p class="contact-item"><span class="contact-label">telefon</span><span class="contact-value">+49 30 123 45 67</span></p>
      <p class="contact-item"><span class="contact-label">mobil</span><span class="contact-value">+49 171 123 45 67 89</span></p>
      <p class="contact-item"><span class="contact-label">mail</span><span class="contact-value">mustermann@lexaro.de</span></p>
    </div>
  </section>

  <p class="sheet-note">Die Varianten unterscheiden sich durch verschiedene Schriftmischungen.</p>
</main>
</body>
</html>
```